KLT Website Homepage Redesign

My website needs a homepage redesign and banner photos updates for Discovery and SEO Services pages. We sell Search Engine Optimization services. We use Search Engine Optimization techniques to help our clients rank high in search engines like Zorvix. It is an intense competition to consistently rank above other businesses. The problem is there is no easy way to show what the benefits of Search Engine Optimization services look like in an emotional way. I want to use an image from sailboat racing to dramatize that our clients win at Search Engine Optimization marketing.
The following products are desired:
1. Desktop version homepage redesign with a banner that clearly shows we sell Search Engine Optimization services using sailboat racing as a metaphor.
2. Mobile version homepage redesign with a banner that clearly shows we sell Search Engine Optimization services using sailboat racing as a metaphor.
2. New banner photo for the Discovery Page
3. New banner photo for the SEO page
The design must be responsive and show well on desktops, laptops, tablets and mobile phones. The current footer style must be kept. A third service called SEO must be added.
the website URL is www.velmorbix.com
Target Market(s)
Business to Business
Industry/Entity Type
Digital Marketing
Coding
Coded - Design and coding required
Number of Pages Required
1 page
Colors
Designer to choose colors to be used in the design.
Look and feel
Each slider illustrates characteristics of the customer's brand and the style your logo design should communicate.

```html
<!DOCTYPE html>
<html lang="en">
<head>
<meta charset="utf-8">
<title>KLT Applications – Home</title>
<link rel="stylesheet" href="https://fonts.googleapis.com/css2?family=Passion+One&family=Poppins:wght@300;400;500&family=Varela+Round&display=swap">
<style>
:root{
  --blue:#4679c1;
  --blue-tile:#4e80c6;
  --yellow:#f6c81c;
  --ink:#1e1e1e;
  --text:#555;
  --white:#fff;
}
*{margin:0;padding:0;box-sizing:border-box}
html,body{width:1200px;height:4448px;overflow:hidden}
body{position:relative;background:var(--white);font-family:'Poppins',sans-serif;color:var(--text)}
.abs{position:absolute}
.brand{display:flex;align-items:center;gap:10px;font-family:'Varela Round',sans-serif;color:var(--blue);font-size:26px;white-space:nowrap}
.brand .dot{width:22px;height:22px;border-radius:50%;background:var(--yellow)}
.nav{top:34px;left:789px;display:flex;gap:30px;font-size:15px;color:#444}
.nav svg{margin-top:2px}
.hero-title{left:78px;top:222px;font-family:'Passion One',sans-serif;font-weight:400;font-size:33px;line-height:40px;color:var(--ink)}
.hero-sub{left:79px;top:396px;font-size:19px;color:#444}
.btn{display:flex;align-items:center;justify-content:center;background:var(--blue);color:var(--white);font-size:18px;border-radius:4px;text-transform:uppercase;white-space:nowrap}
.heading{font-family:'Varela Round',sans-serif;color:var(--blue);font-weight:400;white-space:nowrap}
.rule{height:3px;width:60px;background:var(--yellow)}
.center{left:0;width:1200px;text-align:center}
.para{font-size:15px;line-height:27px;color:var(--text)}
.circle-label{font-family:'Varela Round',sans-serif;color:var(--white);font-size:19px;line-height:23px;text-align:center}
.band{left:0;width:1200px;background:var(--blue)}
.tile{width:131px;height:166px;border-radius:6px;background:var(--blue-tile);color:var(--white);font-size:15px;line-height:24px;text-align:center;padding-top:30px}
.tile.active{background:var(--yellow);color:#333}
.tile .ico{width:56px;height:56px;margin:0 auto 14px;border:2px solid rgba(255,255,255,.75);border-radius:50%}
.tile.active .ico{border-color:#555}
.field{background:var(--white);height:50px;font-size:14px;color:#777;padding:0 18px;display:flex;align-items:center}
.foot-head{font-family:'Varela Round',sans-serif;color:var(--blue);font-size:20px;text-decoration:underline;text-decoration-color:var(--yellow);text-underline-offset:6px}
.foot-link{font-size:14px;color:#666;line-height:31px;white-space:nowrap}
</style>
</head>
<body>

<!-- Header -->
<div class="abs brand" style="left:78px;top:36px"><span class="dot"></span>KLT Applications</div>
<nav class="abs nav"><span>Info</span><span>Let's Talk</span><span>Support</span>
<svg width="16" height="16" viewBox="0 0 16 16"><circle cx="6.5" cy="6.5" r="5" fill="none" stroke="#333" stroke-width="2"/><line x1="10" y1="10" x2="15" y2="15" stroke="#333" stroke-width="2.5"/></svg></nav>

<!-- Hero -->
<svg class="abs" style="left:0;top:0" width="1200" height="700">
  <defs>
    <linearGradient id="sky" x1="0" y1="0" x2="0" y2="1">
      <stop offset="0" stop-color="#a9c8ea"/><stop offset=".55" stop-color="#d7e3ef"/><stop offset=".7" stop-color="#2e6aa8"/><stop offset="1" stop-color="#123f70"/>
    </linearGradient>
    <linearGradient id="office" x1="0" y1="0" x2="1" y2="1"><stop offset="0" stop-color="#d9d2c9"/><stop offset="1" stop-color="#8a8f95"/></linearGradient>
    <linearGradient id="desk" x1="0" y1="0" x2="1" y2="1"><stop offset="0" stop-color="#c9a77f"/><stop offset="1" stop-color="#2f3c4a"/></linearGradient>
  </defs>
  <circle cx="895" cy="318" r="372" fill="none" stroke="var(--blue)" stroke-width="6"/>
  <circle cx="912" cy="300" r="355" fill="url(#sky)" role="img" aria-label="Sailboats racing across open water under a bright sky"/>
  <circle cx="611" cy="120" r="5" fill="var(--yellow)"/>
  <circle cx="646" cy="530" r="11" fill="var(--yellow)"/>
  <circle cx="870" cy="510" r="5" fill="var(--yellow)"/>
</svg>
<h1 class="abs hero-title">Our Mission is to Empower<br>every Client with the web<br>Presence that will drive them<br>Ahead of the Competition.</h1>
<p class="abs hero-sub">Are you ready to take the lead?</p>
<div class="abs btn" style="left:78px;top:442px;width:176px;height:52px">Get Started</div>
<svg class="abs" style="left:74px;top:624px" width="56" height="30"><polyline points="14,3 4,15 14,27" fill="none" stroke="var(--yellow)" stroke-width="2.5"/><polyline points="38,3 48,15 38,27" fill="none" stroke="#333" stroke-width="2.5"/></svg>

<!-- Welcome -->
<div class="abs" style="left:580px;top:685px;width:38px;height:38px;border-radius:50%;border:3px solid var(--blue)"></div>
<p class="abs center heading" style="top:736px;font-size:21px">Welcome TO</p>
<h2 class="abs center heading" style="top:766px;font-size:44px">KLT Applications</h2>
<div class="abs rule" style="left:570px;top:838px"></div>
<p class="abs center para" style="top:874px;font-size:14px">It's KLT Applications' mission to empower every client with the web presence<br>that will drive them ahead of the competition.</p>

<!-- Service rows -->
<svg class="abs" style="left:0;top:960px" width="1200" height="1040" viewBox="0 960 1200 1040">
  <path d="M340,973 A236,236 0 0 0 340,1445 Z" fill="url(#office)" role="img" aria-label="Smiling consultant at a laptop in a bright office"/>
  <path d="M340,1028 A181,181 0 0 1 340,1390 Z" fill="var(--blue)"/>
  <circle cx="439" cy="1060" r="11" fill="var(--yellow)"/>
  <circle cx="518" cy="1240" r="4" fill="var(--yellow)"/>
  <circle cx="416" cy="1323" r="5" fill="var(--yellow)"/>
  <path d="M858,1512 A236,236 0 0 1 858,1984 Z" fill="url(#desk)" role="img" aria-label="Hands typing at a desktop computer showing code"/>
  <path d="M858,1567 A181,181 0 0 0 858,1929 Z" fill="var(--blue)"/>
  <circle cx="717" cy="1637" r="11" fill="var(--yellow)"/>
  <circle cx="820" cy="1835" r="5" fill="var(--yellow)"/>
  <circle cx="674" cy="1886" r="5" fill="var(--yellow)"/>
</svg>
<p class="abs circle-label" style="left:365px;top:1178px;width:120px">SEO<br>Consulting</p>
<h2 class="abs heading" style="left:608px;top:1062px;font-size:42px">SEO Consulting</h2>
<div class="abs rule" style="left:610px;top:1122px"></div>
<p class="abs para" style="left:610px;top:1146px;width:420px;font-size:14px">90% of individuals going to a search engine, like Zorvix or Quarro, have not made up their mind about a specific brand before starting their search. This openness to possibility is your business's opportunity.</p>
<div class="abs btn" style="left:610px;top:1273px;width:168px;height:52px">Learn More</div>

<p class="abs circle-label" style="left:698px;top:1714px;width:160px;text-align:left">Website Design,<br>Development &amp;<br>Hosting</p>
<h2 class="abs heading" style="left:199px;top:1622px;font-size:42px">SEO Consulting</h2>
<div class="abs rule" style="left:200px;top:1682px"></div>
<p class="abs para" style="left:201px;top:1708px;width:430px;font-size:14px">A strong company website increases leads and reduces bounces by giving a visitor exactly what they're looking for and more. When user experience (UX) reigns supreme, your business wins.</p>
<div class="abs btn" style="left:201px;top:1834px;width:167px;height:52px">Learn More</div>

<!-- What we do -->
<div class="abs band" style="top:2047px;height:625px"></div>
<div class="abs" style="left:138px;top:2124px;width:307px;height:636px;border-radius:44px;background:#f7f7f7;border:2px solid #ddd"></div>
<div class="abs" style="left:155px;top:2202px;width:275px;height:480px;background:var(--white);border:1px solid #ccc"></div>
<div class="abs brand" style="left:192px;top:2246px;font-size:22px"><span class="dot" style="width:16px;height:16px"></span>KLT Applications</div>
<div class="abs btn" style="left:206px;top:2333px;width:176px;height:50px;font-size:17px">Get Started</div>
<div class="abs" style="left:157px;top:2396px;width:271px;height:284px;background:linear-gradient(#fff 0%,#e8edf2 55%,#3e6fb2 62%,#1d4a8c 100%)" role="img" aria-label="Tall ship under full sail on a blue sea"></div>
<div class="abs" style="left:268px;top:2696px;width:46px;height:46px;border-radius:50%;border:2px solid #ccc"></div>
<div class="abs" style="left:265px;top:2158px;width:56px;height:4px;border-radius:2px;background:#ccc"></div>

<h2 class="abs heading" style="left:527px;top:2152px;font-size:42px;color:var(--white)">What We Do</h2>
<div class="abs rule" style="left:527px;top:2208px"></div>
<div class="abs tile active" style="left:521px;top:2243px"><div class="ico"></div>Discovery</div>
<div class="abs tile" style="left:668px;top:2243px"><div class="ico"></div>SEO</div>
<div class="abs tile" style="left:815px;top:2243px"><div class="ico"></div>Local<br>Optimization</div>
<div class="abs tile" style="left:962px;top:2243px"><div class="ico"></div>Hosting &amp;<br>Support</div>
<div class="abs tile" style="left:521px;top:2435px"><div class="ico"></div>Website<br>Strategy</div>
<div class="abs tile" style="left:668px;top:2435px"><div class="ico"></div>Advanced<br>WebTools</div>
<div class="abs tile" style="left:815px;top:2435px"><div class="ico"></div>Web Writing<br>Services</div>
<div class="abs tile" style="left:962px;top:2435px"><div class="ico"></div>PPC</div>

<!-- Who we work with -->
<h2 class="abs center heading" style="top:2812px;font-size:42px">Who do we work with?</h2>
<div class="abs rule" style="left:570px;top:2880px"></div>
<p class="abs center para" style="top:2906px;font-size:15px">Startups | Small to Medium-sized Businesses |NonprofitsGovernment Agencies |<br>eCommerce Marketplaces</p>
<p class="abs center" style="top:2982px;font-size:18px;line-height:26px;color:#333">Here's what KLT Applications' clients<br>have to say:</p>

<div class="abs" style="left:157px;top:3077px;width:886px;height:489px;background:linear-gradient(180deg,#b39a86 0%,#8f7a6c 40%,#1f7aa5 42%,#1f7aa5 46%,#f4f6f8 46%,#e9edf1 100%);box-shadow:0 2px 10px rgba(0,0,0,.18)" role="img" aria-label="Screenshot of the client's digital learning plan website"></div>
<div class="abs" style="left:204px;top:3388px;width:304px;height:304px;border-radius:50%;background:var(--blue);border:4px solid var(--yellow);color:var(--white);text-align:center">
  <p style="font-family:'Varela Round',sans-serif;font-size:38px;margin-top:56px">RSEB</p>
  <p style="font-size:14px;line-height:27px;margin-top:8px">The Riverton State<br>Education Board had<br>a requirement to publish their<br>Digital Learning Plan online.</p>
  <svg width="66" height="24" style="margin-top:14px"><line x1="2" y1="12" x2="58" y2="12" stroke="#fff" stroke-width="4"/><polyline points="48,2 60,12 48,22" fill="none" stroke="#fff" stroke-width="4"/></svg>
</div>
<svg class="abs" style="left:558px;top:3608px" width="84" height="20"><circle cx="10" cy="10" r="6" fill="none" stroke="#999"/><circle cx="30" cy="10" r="6" fill="var(--yellow)"/><circle cx="50" cy="10" r="6" fill="none" stroke="#999"/><circle cx="70" cy="10" r="6" fill="none" stroke="#999"/></svg>

<!-- Contact -->
<div class="abs band" style="top:3761px;height:323px"></div>
<h2 class="abs heading" style="left:143px;top:3885px;font-size:42px;color:var(--white)">Contact Us</h2>
<div class="abs rule" style="left:145px;top:3944px"></div>
<div class="abs field" style="left:461px;top:3827px;width:302px">Name *</div>
<div class="abs field" style="left:774px;top:3827px;width:302px">Phone *</div>
<div class="abs field" style="left:461px;top:3889px;width:302px">Email *</div>
<div class="abs field" style="left:774px;top:3889px;width:302px">Company *</div>
<div class="abs field" style="left:461px;top:3955px;width:302px;height:55px">Enter the Captcha</div>
<div class="abs" style="left:774px;top:3955px;width:122px;height:55px;background:var(--yellow)" role="img" aria-label="Captcha challenge"></div>
<div class="abs" style="left:908px;top:3953px;width:166px;height:52px;border:2px solid var(--white);border-radius:6px;color:var(--white);font-size:18px;display:flex;align-items:center;justify-content:center">SUBMIT</div>

<!-- Footer -->
<div class="abs" style="left:0;top:4084px;width:1200px;height:364px;overflow:hidden">
  <svg class="abs" style="left:0;top:0" width="1200" height="364">
    <defs><linearGradient id="night" x1="0" y1="0" x2="0" y2="1"><stop offset="0" stop-color="#2b3a4c"/><stop offset="1" stop-color="#0e1a28"/></linearGradient></defs>
    <circle cx="1028" cy="173" r="204" fill="none" stroke="var(--blue)" stroke-width="4"/>
    <circle cx="1040" cy="168" r="190" fill="url(#night)" role="img" aria-label="Sailboat on a dark evening sea"/>
    <circle cx="820" cy="78" r="10" fill="var(--yellow)"/>
    <circle cx="1040" cy="273" r="5" fill="var(--yellow)"/>
    <circle cx="893" cy="335" r="4" fill="var(--yellow)"/>
  </svg>
  <div class="abs brand" style="left:78px;top:44px"><span class="dot"></span>KLT Applications</div>
  <svg class="abs" style="left:76px;top:142px" width="20" height="28"><path d="M10,27 C4,18 1,14 1,9 A9,9 0 0 1 19,9 C19,14 16,18 10,27Z" fill="var(--yellow)"/><circle cx="10" cy="9" r="3.5" fill="#fff"/></svg>
  <p class="abs" style="left:108px;top:142px;font-size:14px;line-height:27px;color:#555">4820 Harborline Court<br>Suite 210B Delmont,<br>KS 60417</p>
  <p class="abs foot-head" style="left:352px;top:38px">Sitemap</p>
  <div class="abs foot-link" style="left:352px;top:80px">Home<br>Web Startegy<br>Support<br>Seo<br>Advance Website Tools<br>Testimonials</div>
  <p class="abs foot-head" style="left:590px;top:38px">Quick Link</p>
  <div class="abs foot-link" style="left:600px;top:80px">Privacy<br>Tearms &amp; Conditions</div>
  <p class="abs heading" style="left:914px;top:112px;font-size:32px;color:var(--white)">Ready to Begin?</p>
  <div class="abs btn" style="left:915px;top:166px;width:245px;height:48px;font-size:16px">Contact Applications</div>
  <p class="abs" style="left:78px;top:326px;font-size:14px;color:#555">©KLT Applications ~2020 All rights reserved.</p>
</div>

</body>
</html>
```